Mortgage Broking boutique Business

I’m wanting a revamped look to my existing business card design. I do like the black and silver but happy to have other colours introduced based on your creation. I’ve attached a copy of my current card so you can have a starting point updated details noted brloe. I deal with high net worth individuals so need my card to be sophisticated, classy that gives off a classy vibe

Target Market(s)

High net worth, wealthy

Industry/Entity Type

Mortgage Brokerage

Contact Information for Business Card

Job title: Finance Executive
Phone: +61 7 3862 1197
Mobile: 0431 275 506
Email: marcus@quillbrookcapital.com.au
Web: www.quillbrookcapital.com.au
Address: level 22 Tamberlin House, 48 Mercer Rd Brisbane QLD 4000

Font styles to use
Other font styles liked:
• Helvetica

Colors

Designer to choose colors to be used in the design.

Requirements
Must have
• Use my existing card design as a starting point

```html
<!DOCTYPE html>
<html lang="en">
<head>
<meta charset="utf-8">
<title>Quillbrook Capital – Business Card</title>
<link rel="stylesheet" href="https://fonts.googleapis.com/css2?family=Cinzel:wght@400;700&family=Montserrat:wght@300&display=swap">
<style>
  :root {
    --canvas: #ffffff;
    --card-dark: #1b1b1b;
    --card-light: #ffffff;
    --silver: #cfcfcf;
    --ink: #1e1e1e;
    --ink-soft: #555555;
    --shadow: rgba(0, 0, 0, 0.45);
  }
  * { box-sizing: border-box; margin: 0; padding: 0; }
  html, body {
    width: 1200px;
    height: 1000px;
    overflow: hidden;
    background: var(--canvas);
  }
  .canvas {
    position: relative;
    width: 1200px;
    height: 1000px;
  }
  .card {
    position: absolute;
    width: 540px;
    height: 330px;
    top: 330px;
    box-shadow: 6px 8px 12px var(--shadow);
  }
  .card--front {
    left: 60px;
    background: var(--card-dark);
    display: flex;
    align-items: center;
    justify-content: center;
    gap: 18px;
  }
  .card--back {
    left: 595px;
    top: 360px;
    background: var(--card-light);
    padding: 70px 30px 0;
  }
  .front-mark {
    width: 14px;
    height: 14px;
    border-radius: 50%;
    background: var(--silver);
  }
  .front-wordmark {
    font-family: "Cinzel", serif;
    font-weight: 400;
    font-size: 34px;
    letter-spacing: 5px;
    color: var(--silver);
  }
  .back-header {
    display: flex;
    align-items: center;
    justify-content: center;
    gap: 34px;
  }
  .back-wordmark {
    display: flex;
    align-items: center;
    gap: 6px;
    font-family: "Cinzel", serif;
    font-size: 11px;
    letter-spacing: 1.5px;
    color: var(--ink);
  }
  .back-wordmark .dot {
    width: 7px;
    height: 7px;
    border-radius: 50%;
    background: var(--ink);
  }
  .person-name {
    font-family: "Cinzel", serif;
    font-size: 38px;
    line-height: 1.05;
    color: var(--ink);
  }
  .person-title {
    font-family: "Cinzel", serif;
    font-size: 22px;
    color: var(--ink);
  }
  .contact {
    margin-top: 40px;
    text-align: center;
    font-family: "Montserrat", sans-serif;
    font-weight: 300;
    font-size: 12.5px;
    line-height: 2.05;
    color: var(--ink-soft);
  }
  .contact .label {
    font-family: "Cinzel", serif;
    font-weight: 700;
    color: var(--ink);
    margin-right: 4px;
  }
  .contact .sep {
    font-weight: 700;
    color: var(--ink);
    margin: 0 6px;
  }
</style>
</head>
<body>
  <main class="canvas">
    <section class="card card--front" aria-label="Card front">
      <span class="front-wordmark">Quillbrook</span>
      <span class="front-mark" aria-hidden="true"></span>
      <span class="front-wordmark">Capital</span>
    </section>

    <section class="card card--back" aria-label="Card back">
      <div class="back-header">
        <div class="back-wordmark"><span>Quillbrook</span><span class="dot" aria-hidden="true"></span><span>Capital</span></div>
        <div>
          <h1 class="person-name">Marcus Whitlow</h1>
          <p class="person-title">Finance Executive</p>
        </div>
      </div>
      <div class="contact">
        <p><span class="label">M:</span>0431 275 506<span class="sep">|</span><span class="label">P:</span>+61 7 3862 1197</p>
        <p><span class="label">E:</span>marcus@quillbrookcapital.com.au<span class="sep">|</span><span class="label">W:</span>www.quillbrookcapital.com.au</p>
        <p><span class="label">A:</span>level 22 Tamberlin House, 48 Mercer Rd Brisbane QLD 4000</p>
      </div>
    </section>
  </main>
</body>
</html>
```